Marlow & Tate
Business card and stationery design for a management consulting firm  - Consulting
Simple
Benedikt Owen Dolsquin
Lead Consultant
Njegoševa 47 11000 Belgrade
benedikt.owen@marlowtate-example.com
www.marlowtate-example.com
Keep the design clean. "Scandinavian design approach". Address line on business card is preferred not to be included, although if designer finds it to complete the holistic 'picture' of the card, then he/she may use it. Font selection for the rest of the text is up to the designer. Although please note that the font has to be in balance with the logo. Business cards are to be printed on black paper / metal. If printed on paper, the logo part will be with relief printing.
This is designers choice to be creative
dolsquin dolsquin
Tip to designers: Try not to use the monogram "MT" with "Marlow and Tate" on the same side. Printing techniques that will be used are: Embossing / Debossing, Thermography. Keep it clean. Less is more.

```html
<!DOCTYPE html>
<html lang="en">
<head>
<meta charset="utf-8">
<title>Marlow &amp; Tate — Business Card</title>
<link rel="stylesheet" href="https://fonts.googleapis.com/css2?family=Cormorant+Garamond:wght@400&display=swap">
<style>
  :root {
    --canvas-bg: #e6e6e4;
    --card-dark: #141414;
    --card-mid: #262626;
    --card-sheen: #3a3a3a;
    --ink-light: #d9d9d6;
    --ink-soft: #9c9c98;
    --ink-faint: rgba(255, 255, 255, 0.07);
  }
  * { margin: 0; padding: 0; box-sizing: border-box; }
  html, body {
    width: 1200px;
    height: 600px;
    overflow: hidden;
    background: var(--canvas-bg);
    font-family: "Cormorant Garamond", serif;
  }
  .canvas {
    position: relative;
    width: 1200px;
    height: 600px;
  }
  .card {
    position: absolute;
    top: 140px;
    width: 540px;
    height: 320px;
    border-radius: 18px;
    overflow: hidden;
    background: linear-gradient(120deg, var(--card-dark) 0%, var(--card-mid) 38%, var(--card-sheen) 50%, var(--card-mid) 62%, var(--card-dark) 100%);
    box-shadow: 0 6px 18px rgba(0, 0, 0, 0.18);
    color: var(--ink-light);
  }
  .card--front { left: 40px; }
  .card--back { left: 620px; }

  /* Front: brand block */
  .brand {
    position: absolute;
    left: 40px;
    top: 150px;
    width: 210px;
    text-align: center;
  }
  .brand__dot {
    display: block;
    width: 34px;
    height: 34px;
    margin: 0 auto 12px;
    border: 1.5px solid var(--ink-light);
    border-radius: 50%;
  }
  .brand__name {
    font-size: 30px;
    letter-spacing: 0.5px;
    line-height: 1;
  }
  .brand__tag {
    margin-top: 6px;
    font-size: 9px;
    letter-spacing: 5px;
    text-transform: uppercase;
    color: var(--ink-soft);
  }

  /* Front: person & contact */
  .details {
    position: absolute;
    left: 280px;
    top: 48px;
    width: 240px;
  }
  .details__name {
    font-size: 19px;
    line-height: 1.1;
  }
  .details__title {
    font-size: 12px;
    color: var(--ink-soft);
    margin-top: 3px;
  }
  .details__address {
    margin-top: 26px;
    font-size: 11.5px;
    line-height: 1.45;
    color: var(--ink-soft);
  }
  .contact {
    list-style: none;
    margin-top: 34px;
    font-size: 11px;
    line-height: 1.6;
    color: var(--ink-soft);
  }
  .contact__label {
    display: inline-block;
    width: 20px;
    color: var(--ink-light);
  }

  /* Back */
  .back__mark {
    position: absolute;
    left: 60px;
    top: 40px;
  }
  .back__brand {
    position: absolute;
    right: 18px;
    top: 50%;
    transform: translate(50%, -50%) rotate(-90deg) translateY(-50%);
    transform-origin: center;
    white-space: nowrap;
    text-align: center;
  }
  .back__brand .brand__name { font-size: 32px; }
</style>
</head>
<body>
<main class="canvas">

  <section class="card card--front" aria-label="Business card front">
    <div class="brand">
      <span class="brand__dot"></span>
      <div class="brand__name">Marlow and Tate</div>
      <div class="brand__tag">Consulting</div>
    </div>

    <div class="details">
      <p class="details__name">Benedikt Owen Dolsquin</p>
      <p class="details__title">Lead Consultant</p>
      <p class="details__address">Njegoševa 47<br>11000 Belgrade</p>
      <ul class="contact">
        <li><span class="contact__label">T</span>+381 60 555 0142</li>
        <li><span class="contact__label">E</span>benedikt.owen@marlowtate-example.com</li>
        <li><span class="contact__label">W</span>www.marlowtate-example.com</li>
      </ul>
    </div>
  </section>

  <section class="card card--back" aria-label="Business card back">
    <svg class="back__mark" width="240" height="240" viewBox="0 0 240 240" aria-hidden="true">
      <circle cx="120" cy="120" r="110" fill="none" stroke="var(--ink-faint)" stroke-width="14"/>
    </svg>
    <div class="back__brand">
      <div class="brand__name">Marlow and Tate</div>
      <div class="brand__tag">Consulting</div>
    </div>
  </section>

</main>
</body>
</html>
```